Corporate Design für IT-Dienstleister
Hallo Designer,
meine Entscheidung ist getroffen - es kann ja leider nur einer gewinnen.
Nochmals vielen Dank für die Einsendungen.
Schöne Grüße
Hallo zusammen,
ich möchte mich bei allen Designer noch mal für die vielen wirklich toll gelungenen und kreativen Vorschläge bedanken. Für die jetzt ausstehende Entscheidung möchte ich mir noch eine Nacht Zeit lassen - wobei ich sagen muss die noch verbliebenen Designs gefallen mir alle super.
Vielen Dank
@tivmolk
ich wurde auch per pn darauf hingewiesen und habe deshalb aussortiert :-/
@Pluvia Dm
zu #97 die Visitenkarte trifft es auf den Punkt. Sie wirkt elegant, klar und professionell sowie modern - super... Das Logo ist mir noch nicht ausdrucksstark genug. Vielleicht können Sie noch ein paar Alternativen (mit der gleichen Visitenkarte) vorschlagen? (Wenn Sie möchten, könne Sie auch gerne andere Farben verwenden!) Wie würde das Briefpapier aussehen?
Danke und wirklich gute Arbeit, bin gespannt...
Gruß wolkenbaer
ich bin mir noch nicht ganz sicher ob das richtige bisher dabei war.
Vielleicht hat jemand noch eine Idee für ein "einfaches" Logo.
Evtl. könnte man das Logo weglassen und mit dem "L" von "Brodhagen" irgendetwas anfangen???
Ich freue mich auf weitere Vorschläge
vielen Dank für die wirklich tollen bisherigen Vorschläge. Einige von diesen kommen bereits jetzt schon in die engere Auswahl.
Ich würde jetzt gerne noch einige Vorschläge sehen, die nicht auf den bisherigen Farben/Formen basieren und auch nicht unbedingt mit meinen Angaben im Briefing übereinstimmen. Welches Design würden Sie mir empfehlen oder welche Farben, Formen, Schriften etc. würden Sie für meine angebotenen Dienstleistungen verwenden?
Ich freue mich auf Ihre Vorschläge
MfG wolkenbaer
zu #79 und #80
sieht interessant aus... wie würde visitenkarte und geschäftspapier aussehen?
gruß wolkenbaer
#61 Die Visitenkarte finde ich top :-) - Allerdings habe ich teilweise die Rückmeldung bekommen dass es zu bunt wirkt (Meine Worte in quillbrankets Ohren) Vielleicht die Balken weg und dafür was schlichteres ?
#59 Das Geschäftspapier ist irgendwie noch nicht rund - Kann es mir auch nicht so richtig vorstellen, da da in der Mitte die Visitenkarte ist - und leider kein Text :-/
@tkgrafik
zu#46 und #47
Logo finde ich cool, vor allem die schwarze Visitenkarte ist mal was anderes und bleibt den Kunden nach der Übergabe in Erinnerung... Ich frage mich wie man diese "Besonderheit" beim Gschäftspapier mit überträgt? Wie würde die Rückseite der Visitenkarte aussehen?
@BLoomiqPX
zu #54, #55, #56
ich fand die Farbverteilung vorher besser (web rot, tele grün, pm blau) -
zu #55
Oben die Reiter auf der linken Seite sehen super aus. Leider auch mit der falschen Farbverteilung.
#57 und #58 sind mir zu blass
@vantrel:
vielen Dank für die vielen unterschiedlichen Ausführungen. Leider war bis jetzt noch nicht das richtige dabei!
@ BLoomiqPX:
#34 Das Logo ist super und kommt auf jeden Fall in kombi mit der Visitenkarte und dem Geschäftspapier die engere Auswahl. Schrit, Logo und Farben passen gut. Dieses Angebot ist aktuell mein Favorit!!!
#44 Gefällt mir auch sehr gut, haben Sie vielleicht noch weitere alternative Ideen von der Anordnung? Ich finde es sieht oben links bzw. mittig ein wenig leer aus! Den Balken unten finde ich super. Vielleicht könnte man auch mittig im Blatt mit Wasserzeichen arbeiten? Sieht dann aber vielleicht auch überladen aus! Mal schauen...
#45 Visitenkarte - kommt richtig gut! Nur die Anordung der Farben ist dann ja auf der Rückseite falsch rum. Würde ich mir gerne auch noch andersrum anschauen.
Danke und Gruß wolkenbaer
@BloomiqPX
zu #31, #32, #33
Das Logo gefällt mir richtig gut.
Als Slogan bitte mal mit "web.telefonie.projektmanagement" probieren und eine rundere weichere Schrift. Am besten gefällt mir #31 vor allem, weil das Logo über dem Namen steht und die gesammte Optik dann nicht so lang gezogen ist. Das macht sich dann bestimmt auch auf der Visitenkarte ganz gut. Mit den Farben - ob das IT nun blau ist oder nicht und welches Feld welche Farbe hat - müsste man noch mal schauen... Evtl. blau oben für Projektmanagement, web rot, telefonie grün - oder was meinst Du? Danke wolkenbaer
@vantrel
#28 ist ein gelungenes Logo und kommt in die engere Auswahl. Die Schrift + Logo etc. passen gut zusammen und gefallen mir.
#26 und #30
Der Würfel ist mir zu eckig, zu groß und die Symbole nicht modern genug.
@all
Vielen Dank für die bisherigen Vorschläge, die mir auch schon sehr gut gefallen.
Bisher fehlt mir bei den Logo's leider noch der Bezug zu meinem Unternehmen.
Ich biete 3 Dienstleistungen an (siehe Briefing), diese könnten ja z.B. in dem Logo durch Symbole dargestellt werden. Beispiel: 3d Würfel auf jeder Seite ein Symbol eingestanzt (@, telefonhörer, stift o.ä.)
Schönen Gruß wolkenbaer
zu #18
Die Schrift entspricht wie auch schon im ersten Entwurf genau meiner Vorstellung. Auch das Pipe-Symbol zwischen Namen und IT finde ich super. Dadurch wird das ganze ein wenig aufgelockert. Mein Name ist ja auch nicht gerade kurz :-) Bei dem Logo finde ich einfach keinen Zusammenhang mit meinen Dienstleistungen. Vielleicht den Slogan statt mit Punkten mit mittigen Punkten oder auch mit pipe's trennen!? Gruß
zu #16
Danke für die Aktualisierung. Kann die Schrift noch etwas weicher gestaltet werden? Und dann vielleicht im direkten Vergleich mit dem "alten" Slogan? Danke
zu #7, #8, #9, #10, #14, #15, #17
Danke für die vielen Vorschläge. Bisher ist leider noch nicht das richtige dabei. Die eingereichten Vorschläge sind mir eher noch zu einfach und nicht ausdrucksstark genug.
zu #12 und #13
Das Logo von #12 ist interessant und hat einen guten Wiedererkennungswert. Es sieht dynamisch aus. Farben sind auch gut. Evtl. den Namen auch mit großem Anfangsbuchstaben L und den Slogan wie bei #13.
zu #6 und #5
Ich finde auf dem Geschäftspapier den senkrechten Strich auf der linken Seite gut.
Das Logo sieht mir zu sehr nach CD Rom o.ä. aus. Da ich kein "PC-Schrauber" bin möchte ich keine EDV Komponenten in dem Logo haben. Die Schrift und die Farbe wirken (in Kombination) eher kalt. Ich will einen freundlichen Eindruck bei meinen Kunden hinterlassen.
zu #3
mit den 3 Symbolen hinter dem Namen kann ich leider nichts anfangen. Mir fehlt dadurch auch der Wiedererkennungswert. Die Farben sind mir zu stark. Das Logo wirkt insgesamt nicht innovativ genug.
zu #1
Das Design gefällt mir gut und geht auf jeden Fall in die richtige Richtung.
Die Farbauswahl sowie der Aufbau ist entspricht meinen Vorstellungen.
Die Ringe sind noch nicht das richtige Motiv.
Der Slogan web.telefonie.projektmanagement ist super. :-)
Vielleicht würde es auch ganz gut aussehen, wenn das Motiv über dem Namen steht, dann zieht sich das ganze nicht so in die Länge!?
wie von zurhalwig schon richtig interpretiert, bin ich auf der Suche nach einem neuen CI.
Daher bitte nicht die Farben o.ä. von meiner bisherigen Webseite übernehmen.
Von den Farben her stelle ich mir - wie in der Auftragsbeschreibung angegeben - eher etwas schlicht gehaltenes vor. Gruß wolkenbaer

```html
<!DOCTYPE html>
<html lang="de">
<head>
<meta charset="utf-8">
<title>Brodhagen IT – Geschäftsausstattung</title>
<link rel="stylesheet" href="https://fonts.googleapis.com/css2?family=Source+Sans+3:wght@400;600;700&display=swap">
<style>
  :root {
    --brand-blue: #159ddc;
    --brand-blue-light: #7cc8ee;
    --paper: #ffffff;
    --canvas: #ffffff;
    --text-grey: #6b6b6b;
    --text-dark: #3c3c3c;
    --shadow: rgba(0, 0, 0, 0.32);
    --window-fill: #efefef;
    --window-edge: #c9c9c9;
  }
  * { box-sizing: border-box; margin: 0; padding: 0; }
  html, body {
    width: 780px; height: 1200px; overflow: hidden;
    background: var(--canvas);
    font-family: "Source Sans 3", "Myriad Pro", sans-serif;
  }
  .stationery { position: relative; width: 780px; height: 1200px; }

  .sheet {
    position: absolute;
    background: var(--paper);
    box-shadow: 7px 7px 6px var(--shadow);
    overflow: hidden;
  }

  /* Wordmark stand-in */
  .wordmark { position: absolute; display: flex; flex-direction: column; gap: 2px; }
  .wordmark-row { display: flex; align-items: center; gap: 8px; }
  .wordmark-square { width: 16px; height: 16px; background: var(--brand-blue); }
  .wordmark-name {
    font-weight: 700; color: var(--brand-blue);
    font-size: 21px; letter-spacing: 1.5px; text-transform: uppercase; line-height: 1;
  }
  .wordmark-tagline {
    font-size: 8px; letter-spacing: 1.4px; color: var(--brand-blue);
    text-transform: uppercase; padding-left: 24px; line-height: 1;
  }

  /* Business card front */
  .card-front { left: 82px; top: 8px; width: 330px; height: 210px; }
  .card-front .wordmark { left: 40px; top: 34px; }
  .card-holder {
    position: absolute; left: 92px; top: 106px;
    font-size: 13px; color: var(--text-grey);
  }
  .card-holder strong { color: var(--text-dark); font-weight: 600; }
  .card-contact {
    position: absolute; left: 14px; top: 158px; right: 12px;
    display: grid; grid-template-columns: 78px 132px 1fr;
    font-size: 8.5px; line-height: 12px; color: var(--text-grey);
  }
  .card-contact .label { color: var(--brand-blue); font-weight: 700; margin-right: 3px; }
  .card-contact .address { padding-top: 12px; }

  /* Business card back */
  .card-back { left: 82px; top: 235px; width: 323px; height: 203px; background: var(--brand-blue); }
  .card-back .motif {
    position: absolute; left: 0; top: 0; width: 75px; height: 100%;
    background: linear-gradient(90deg, var(--brand-blue-light), var(--brand-blue));
  }

  /* Envelope */
  .envelope { left: 8px; top: 393px; width: 760px; height: 380px; }
  .envelope .wordmark { left: 120px; top: 94px; }
  .address-window {
    position: absolute; left: 67px; top: 155px; width: 323px; height: 157px;
    border-radius: 16px; background: linear-gradient(180deg, #f7f7f7, var(--window-fill));
    border: 1px solid var(--window-edge);
    box-shadow: 3px 4px 4px rgba(0,0,0,0.25);
  }

  /* Letterhead */
  .letterhead { left: 8px; top: 802px; width: 760px; height: 383px; }
  .letterhead .wordmark { left: 120px; top: 95px; }

  .motif-band {
    position: absolute; right: 0; top: 30px; width: 128px; bottom: 0;
    background: radial-gradient(circle at 72% 55%, var(--brand-blue) 0%, var(--brand-blue-light) 55%, #d6eefb 100%);
  }
</style>
</head>
<body>
<main class="stationery">

  <section class="sheet card-front" aria-label="Visitenkarte Vorderseite">
    <div class="wordmark">
      <div class="wordmark-row"><span class="wordmark-square"></span><span class="wordmark-name">Brodhagen IT</span></div>
      <span class="wordmark-tagline">Web | Telefonie | Projektmanagement</span>
    </div>
    <p class="card-holder">Jonas <strong>Brodhagen</strong></p>
    <div class="card-contact">
      <div class="address">Lindenweg 12<br>23899 Feldhusen</div>
      <div>
        <span class="label">T</span>+49 (0)1234 . 567 80 10<br>
        <span class="label">F</span>+49 (0)1234 . 567 80 11<br>
        <span class="label">M</span>+49 (0)170 . 24 68 135
      </div>
      <div class="address">info@brodhagen-it.de<br>www.brodhagen-it.de</div>
    </div>
  </section>

  <section class="sheet card-back" aria-label="Visitenkarte Rückseite">
    <div class="motif" role="img" aria-label="Konzentrisches Ringmotiv in hellem Blau"></div>
  </section>

  <section class="sheet envelope" aria-label="Briefumschlag mit Fenster">
    <div class="wordmark">
      <div class="wordmark-row"><span class="wordmark-square"></span><span class="wordmark-name">Brodhagen IT</span></div>
      <span class="wordmark-tagline">Web | Telefonie | Projektmanagement</span>
    </div>
    <div class="address-window"></div>
    <div class="motif-band" role="img" aria-label="Blaues konzentrisches Ringmotiv am rechten Rand"></div>
  </section>

  <section class="sheet letterhead" aria-label="Briefbogen">
    <div class="wordmark">
      <div class="wordmark-row"><span class="wordmark-square"></span><span class="wordmark-name">Brodhagen IT</span></div>
      <span class="wordmark-tagline">Web | Telefonie | Projektmanagement</span>
    </div>
    <div class="motif-band" role="img" aria-label="Blaues konzentrisches Ringmotiv am rechten Rand"></div>
  </section>

</main>
</body>
</html>
```